Design a Flyer for Quill Parlour

Hi

I want 2 flyers designed for a new tattoo studio. First design I know exactly what I [url removed, login to view] the information is below. Second design i am open to your ideas. I will pay 40 GBP for each design

Front page
Logo as attached. On the page "Flyer front" this is an example of how I exactly want the background colour (the light colour). I want it to be simple, you can design the rest

Back page

I want to use the template layout "flyer back" for where I want a picture and text. Attached is the graphic of the girl. Below is the text for under the main picture. I will provide you with all the text later in the contest. I will make is about as much as is in the example template

Studio tatua?u inne ni? wszystkie (similar to the red font on the template example)

W przeciwie?stwie do ubra?, tatua?e nie mog? by? wyrzucone, upchni?te na dno szafy czy oddane je?li Ci si? znudz? ... wi?c je?li my?lisz o ozdobieniu swojego cia?a, zrób to u najlepszych!
W naszym studiu nie tylko poczujesz si? jak w salonie pi?kno?ci, b?ogo i wygodnie, nasz personel przedstawi Ci te? najnowsze trendy i doradzi "w czym" b?dzie Ci naj?adniej.

Odwied? nas w naszym studiu w centrum Katowic a przekonasz si? na w?asnej skórze.

Second design I want an original design only using the logo. I can provide the text when I see the design. The style of the flyer should be:

Elegant
Expensive
For people who don't have a tattoo yet
More for men than women

I will make a decision as soon as possible

```html
<!DOCTYPE html>
<html lang="pl">
<head>
<meta charset="utf-8">
<title>Quill Parlour – flyers</title>
<link href="https://fonts.googleapis.com/css2?family=Anton&family=Great+Vibes&family=Playfair+Display:wght@700;900&family=Raleway:wght@300;400;700&display=swap" rel="stylesheet">
<style>
  :root {
    --ink: #111111;
    --night: #0c0c0c;
    --paper: #e4e4e4;
    --white: #ffffff;
    --red: #d9161d;
    --grey-text: #9a9a9a;
    --skull-tone: #2a2a2a;
    --gap: #ffffff;
  }
  * { margin: 0; padding: 0; box-sizing: border-box; }
  html, body { width: 1200px; height: 560px; overflow: hidden; background: var(--gap); }
  .canvas { position: relative; width: 1200px; height: 560px; }
  .flyer { position: absolute; top: 0; height: 560px; overflow: hidden; }

  /* Front – script */
  .flyer--script { left: 0; width: 396px; background: var(--ink); }
  .corner-flourish { position: absolute; width: 34px; height: 34px; background: #2b2b2b; }
  .corner-flourish--tl { top: 6px; left: 6px; }
  .corner-flourish--tr { top: 6px; right: 6px; }
  .corner-flourish--bl { bottom: 6px; left: 6px; }
  .corner-flourish--br { bottom: 6px; right: 6px; }
  .side-diamond { position: absolute; top: 276px; width: 10px; height: 10px; background: var(--red); transform: rotate(45deg); }
  .side-diamond--left { left: -3px; }
  .side-diamond--right { right: -3px; }
  .script-title { position: absolute; top: 20px; left: 0; width: 100%; text-align: center; line-height: 1; }
  .script-title__get { display: block; font-family: "Playfair Display", serif; font-weight: 900; font-size: 96px; color: var(--white); letter-spacing: -2px; }
  .script-title__that { display: block; font-family: "Great Vibes", cursive; font-size: 112px; color: var(--red); margin-top: -8px; }
  .script-title__tattoo { display: block; font-family: "Playfair Display", serif; font-weight: 900; font-size: 92px; color: var(--white); margin-top: -14px; letter-spacing: -2px; }

  /* Shared brand lockup */
  .brand { position: absolute; left: 0; width: 100%; display: flex; justify-content: center; align-items: center; gap: 12px; }
  .brand__mark { display: flex; align-items: center; gap: 6px; }
  .brand__dot { width: 16px; height: 16px; border-radius: 50%; background: currentColor; }
  .brand__name { font-family: "Raleway", sans-serif; font-weight: 700; font-size: 22px; line-height: 1; }
  .brand__divider { width: 1px; height: 64px; background: currentColor; }
  .brand__tagline { font-family: "Raleway", sans-serif; font-weight: 400; font-size: 17px; line-height: 1.1; }
  .flyer--script .brand { top: 438px; color: var(--white); }

  /* Front – bold */
  .flyer--bold { left: 407px; width: 388px; background: var(--paper); }
  .bold-title { position: absolute; top: 14px; left: 0; width: 100%; text-align: center; font-family: "Anton", sans-serif; line-height: 0.92; color: var(--ink); }
  .bold-title__get { display: block; font-size: 88px; }
  .bold-title__that { display: block; font-size: 88px; color: var(--red); }
  .bold-title__tat, .bold-title__too { display: block; font-size: 142px; }
  .flyer--bold .brand { top: 440px; color: var(--ink); }

  /* Back */
  .flyer--back { left: 804px; width: 396px; background: var(--night); color: var(--white); font-family: "Raleway", sans-serif; }
  .skull-art { position: absolute; left: 40px; top: 40px; width: 316px; height: 480px; border-radius: 48% 48% 42% 42%; background: radial-gradient(ellipse at 50% 40%, var(--skull-tone) 0%, #1c1c1c 55%, var(--night) 80%); }
  .back-heading { position: absolute; top: 12px; left: 0; width: 100%; text-align: center; font-weight: 300; font-size: 20px; color: var(--red); }
  .back-copy { position: absolute; top: 52px; left: 24px; right: 24px; font-weight: 400; font-size: 13.4px; line-height: 1.55; text-align: justify; }
  .back-visit { position: absolute; top: 248px; left: 36px; right: 36px; text-align: center; font-size: 13.4px; line-height: 1.45; }
  .artists { position: absolute; top: 322px; left: 20px; right: 20px; display: flex; justify-content: space-between; }
  .artist { width: 96px; text-align: center; }
  .artist__name { font-weight: 700; font-size: 10.5px; line-height: 1.25; text-transform: uppercase; }
  .artist__note { margin-top: 5px; font-size: 6.5px; color: var(--grey-text); line-height: 1.3; }
  .hours { position: absolute; top: 408px; left: 0; width: 100%; text-align: center; }
  .hours__title { font-size: 15px; color: var(--red); text-transform: uppercase; letter-spacing: 0.5px; }
  .hours__line { margin-top: 12px; font-weight: 700; font-size: 11.5px; }
  .contact { position: absolute; bottom: 14px; font-size: 8.5px; color: var(--grey-text); line-height: 1.3; }
  .contact--left { left: 12px; }
  .contact--right { right: 12px; text-align: left; }
</style>
</head>
<body>
<main class="canvas">

  <section class="flyer flyer--script">
    <div class="corner-flourish corner-flourish--tl" role="img" aria-label="corner ornament"></div>
    <div class="corner-flourish corner-flourish--tr" role="img" aria-label="corner ornament"></div>
    <div class="corner-flourish corner-flourish--bl" role="img" aria-label="corner ornament"></div>
    <div class="corner-flourish corner-flourish--br" role="img" aria-label="corner ornament"></div>
    <span class="side-diamond side-diamond--left"></span>
    <span class="side-diamond side-diamond--right"></span>
    <h1 class="script-title">
      <span class="script-title__get">get</span>
      <span class="script-title__that">that</span>
      <span class="script-title__tattoo">tattoo</span>
    </h1>
    <div class="brand">
      <div class="brand__mark"><span class="brand__dot"></span><span class="brand__name">Quill Parlour</span></div>
      <span class="brand__divider"></span>
      <p class="brand__tagline">body art<br>tattoo<br>studio</p>
    </div>
  </section>

  <section class="flyer flyer--bold">
    <h1 class="bold-title">
      <span class="bold-title__get">GET</span>
      <span class="bold-title__that">THAT</span>
      <span class="bold-title__tat">TAT</span>
      <span class="bold-title__too">TOO</span>
    </h1>
    <div class="brand">
      <div class="brand__mark"><span class="brand__dot"></span><span class="brand__name">Quill Parlour</span></div>
      <span class="brand__divider"></span>
      <p class="brand__tagline">body art<br>tattoo<br>studio</p>
    </div>
  </section>

  <section class="flyer flyer--back">
    <div class="skull-art" role="img" aria-label="faint sugar skull illustration in the background"></div>
    <h2 class="back-heading">Studio tatua?u inne ni? wszystkie</h2>
    <p class="back-copy">W przeciwie?stwie do ubra?, tatua?e nie mog? by? wyrzucone, upchni?te na dno szafy czy oddane je?li Ci si? znudz? ... wi?c je?li my?lisz o ozdobieniu swojego cia?a, zrób to u najlepszych! W naszym studiu nie tylko poczujesz si? jak w salonie pi?kno?ci, b?ogo i wygodnie, nasz personel przedstawi Ci te? najnowsze trendy i doradzi "w czym" b?dzie Ci naj?adniej.</p>
    <p class="back-visit">Odwied? nas w naszym studiu w centrum Katowic a przekonasz si? na w?asnej skórze.</p>
    <div class="artists">
      <div class="artist"><p class="artist__name">Marek<br>Halloway</p><p class="artist__note">Few details regarding artist if provided</p></div>
      <div class="artist"><p class="artist__name">Clara<br>Wenton</p><p class="artist__note">Few details regarding artist if provided</p></div>
      <div class="artist"><p class="artist__name">Tomas<br>Bredley</p><p class="artist__note">Few details regarding artist if provided</p></div>
    </div>
    <div class="hours">
      <p class="hours__title">Walk ins and appointments</p>
      <p class="hours__line">weekdays 11am - 7pm</p>
      <p class="hours__line">saturdays 2pm - 10pm</p>
    </div>
    <p class="contact contact--left">quillparlour.example<br>555 018 2746</p>
    <p class="contact contact--right">18 Ember Lane north<br>brookfield</p>
  </section>

</main>
</body>
</html>
```